Roof wash and Gutter Cleaning

Would like to see our colors and logo incorporated into design along with phone number and before/after picture(s). We use a non pressure softwash process we use unlike high pressure. We are a exterior cleaning company that likes to set our standards high with safe methods to cleaning the everyday surfaces on homes.
“Serving the Tri-State Area”
A list of our services:
House washing
Shingle and metal roof washing
Deck cleaning
Window cleaning
Concrete cleaning
Gutter cleaning
514-362-0917
We do not need the address section as these will be more for our meet and greets. As well handed out as clipped door  postcards.

Shingle roof wash and gutter cleaning

```html
<!DOCTYPE html>
<html lang="en">
<head>
<meta charset="utf-8">
<title>Summit Exterior Cleaning – Postcard</title>
<link href="https://fonts.googleapis.com/css2?family=Inter:wght@500;600;700;800&family=Montserrat:ital,wght@0,600;0,700;1,700&family=Kaushan+Script&display=swap" rel="stylesheet">
<style>
  :root{
    --board:#a7a7a7;
    --label:#d9d9d9;
    --white:#ffffff;
    --navy:#15304f;
    --blue:#2f6fbd;
    --blue-deep:#1f5aa8;
    --blue-light:#5b9be0;
    --mist:#e7eff8;
    --green:#5aac44;
  }
  *{box-sizing:border-box;margin:0;padding:0}
  html,body{width:882px;height:1200px;overflow:hidden;background:var(--board)}
  .board{position:relative;width:900px;height:1224px;transform:scale(0.98);transform-origin:0 0;background:var(--board);font-family:"Inter",sans-serif}
  .side-label{position:absolute;left:0;width:900px;text-align:center;font:600 11px "Inter",sans-serif;letter-spacing:.5px;color:var(--label)}
  .card{position:absolute;left:28px;width:845px;height:563px;background:var(--white);overflow:hidden}
  .card--front{top:34px}
  .card--back{top:633px}
  .abs{position:absolute}
  .layer{position:absolute;left:0;top:0;width:845px;height:563px}

  /* front */
  .brand{left:30px;top:62px;width:270px;color:var(--blue)}
  .brand__row{display:flex;align-items:center;gap:12px}
  .brand__dot{width:34px;height:34px;border-radius:50%;background:var(--green)}
  .brand__name{font:700 50px/1 "Inter",sans-serif;color:var(--blue)}
  .brand__tag{margin-top:14px;font:700 12px/1.2 "Inter",sans-serif;color:var(--blue)}
  .eyebrow{left:0;width:845px;top:222px;text-align:center;font:700 19px "Montserrat",sans-serif;letter-spacing:4px;color:var(--navy)}
  .headline{left:0;width:845px;top:243px;text-align:center;font:400 50px/1.1 "Kaushan Script",cursive;color:var(--blue)}
  .services{list-style:none;font:500 24px/33px "Inter",sans-serif;color:var(--navy)}
  .services li{display:flex;align-items:center;gap:14px}
  .services svg{flex:none}
  .services--left{left:30px;top:343px}
  .services--right{left:525px;top:343px}
  .area{left:57px;top:520px;font:italic 700 19px "Montserrat",sans-serif;letter-spacing:1px;color:var(--white)}
  .contact-icon{left:680px;top:457px;width:30px;height:30px;border-radius:50%;background:var(--green);display:flex;align-items:center;justify-content:center}
  .contact-label{left:652px;top:494px;font:600 9px "Inter",sans-serif;letter-spacing:.5px;color:var(--navy)}
  .phone{left:571px;top:506px;font:700 35px "Montserrat",sans-serif;color:var(--white)}

  /* back */
  .back-eyebrow{left:0;width:845px;top:36px;text-align:center;font:700 16px "Montserrat",sans-serif;letter-spacing:3px;color:var(--white)}
  .back-title{left:0;width:845px;top:56px;text-align:center;font:700 37px "Inter",sans-serif;color:var(--white)}
  .tile{position:absolute;width:192px;height:134px;overflow:hidden}
  .tile__photo{position:absolute;inset:0}
  .tile__tag{position:absolute;left:0;top:0;background:var(--white);border-radius:0 0 9px 0;padding:3px 9px 4px 9px;font:700 9.5px "Inter",sans-serif;color:var(--navy)}
  .photo--siding-before{background:linear-gradient(160deg,#8e8f85 0%,#c8c6b4 45%,#a7a494 100%)}
  .photo--siding-after{background:linear-gradient(160deg,#9fc0dc 0%,#dcd8be 40%,#c8c2a0 100%)}
  .photo--gutter-before{background:linear-gradient(150deg,#6d5440 0%,#a0876a 45%,#5b4634 100%)}
  .photo--gutter-after{background:linear-gradient(150deg,#6d6a66 0%,#b8bcb6 45%,#4f7467 100%)}
  .photo--stone-before{background:linear-gradient(180deg,#5b5248 0%,#9a8a76 50%,#4d443b 100%)}
  .photo--stone-after{background:linear-gradient(180deg,#6a5848 0%,#b39676 50%,#594838 100%)}
  .photo--deck-before{background:linear-gradient(180deg,#d6d3c6 0%,#8a6e52 60%,#6b513a 100%)}
  .photo--deck-after{background:linear-gradient(180deg,#cfc9b3 0%,#a9703b 60%,#7a4a20 100%)}
  .intro{left:34px;top:492px;width:560px;font:500 19.5px/1.3 "Inter",sans-serif;color:var(--navy)}
  .mini-brand{left:700px;top:510px;display:flex;align-items:center;gap:8px}
  .mini-brand .brand__dot{width:20px;height:20px}
  .mini-brand span{font:700 28px "Inter",sans-serif;color:var(--blue)}
</style>
</head>
<body>
<div class="board">
  <div class="side-label" style="top:17px">FRONT</div>

  <section class="card card--front">
    <svg class="layer" viewBox="0 0 845 563" aria-hidden="true">
      <defs>
        <linearGradient id="waveBlue" x1="0" y1="0" x2="1" y2="0">
          <stop offset="0" stop-color="#2c67b5"/><stop offset=".6" stop-color="#4d8fd8"/><stop offset="1" stop-color="#2d68b6"/>
        </linearGradient>
      </defs>
      <path d="M0 250 C120 205 220 240 300 225 C420 200 520 255 620 240 C720 225 790 250 845 235 L845 563 L0 563 Z" fill="var(--mist)"/>
      <path d="M0 448 C90 430 180 450 270 475 C360 500 430 505 520 470 C600 440 700 435 845 450 L845 563 L0 563 Z" fill="url(#waveBlue)"/>
      <path d="M215 305 C320 295 470 300 625 306" stroke="var(--green)" stroke-width="5" fill="none" stroke-linecap="round"/>
    </svg>

    <svg class="layer" viewBox="0 0 845 563" role="img" aria-label="Photo of a rinsed translucent corrugated roof panel">
      <defs>
        <linearGradient id="roofPhoto" x1="0" y1="0" x2="1" y2="1">
          <stop offset="0" stop-color="#51707f"/><stop offset=".5" stop-color="#1f9a9c"/><stop offset="1" stop-color="#2b8f93"/>
        </linearGradient>
      </defs>
      <path d="M500 0 L845 0 L845 225 C800 255 740 262 690 255 C610 245 545 190 520 120 C505 80 500 40 500 0 Z" fill="var(--blue)"/>
      <path d="M512 0 L845 0 L845 215 C800 245 745 250 695 243 C620 232 560 180 535 115 C520 78 514 40 512 0 Z" fill="url(#roofPhoto)"/>
      <path d="M618 0 C615 90 680 190 845 215" stroke="var(--white)" stroke-width="2" fill="none"/>
    </svg>

    <div class="abs brand">
      <div class="brand__row"><span class="brand__dot"></span><span class="brand__name">Summit</span></div>
      <div class="brand__tag">Exterior Cleaning &amp; Maintenance Co.</div>
    </div>

    <div class="abs eyebrow">NON PRESSURE</div>
    <div class="abs headline">Softwash Cleaning</div>

    <ul class="abs services services--left">
      <li><svg width="22" height="18" viewBox="0 0 22 18"><path d="M2 9 L8 15 L20 3" stroke="var(--green)" stroke-width="4" fill="none"/></svg>House Washing</li>
      <li><svg width="22" height="18" viewBox="0 0 22 18"><path d="M2 9 L8 15 L20 3" stroke="var(--green)" stroke-width="4" fill="none"/></svg>Shingle and Metal Roof Washing</li>
      <li><svg width="22" height="18" viewBox="0 0 22 18"><path d="M2 9 L8 15 L20 3" stroke="var(--green)" stroke-width="4" fill="none"/></svg>Deck Cleaning</li>
    </ul>
    <ul class="abs services services--right">
      <li><svg width="22" height="18" viewBox="0 0 22 18"><path d="M2 9 L8 15 L20 3" stroke="var(--green)" stroke-width="4" fill="none"/></svg>Window Cleaning</li>
      <li><svg width="22" height="18" viewBox="0 0 22 18"><path d="M2 9 L8 15 L20 3" stroke="var(--green)" stroke-width="4" fill="none"/></svg>Concrete Cleaning</li>
      <li><svg width="22" height="18" viewBox="0 0 22 18"><path d="M2 9 L8 15 L20 3" stroke="var(--green)" stroke-width="4" fill="none"/></svg>Gutter Cleaning</li>
    </ul>

    <div class="abs area">SERVING THE TRI-STATE AREA</div>
    <div class="abs contact-icon">
      <svg width="16" height="16" viewBox="0 0 24 24"><path d="M6.6 10.8a15 15 0 0 0 6.6 6.6l2.2-2.2c.3-.3.7-.4 1-.2 1.1.4 2.3.6 3.6.6.6 0 1 .4 1 1V20c0 .6-.4 1-1 1A17 17 0 0 1 3 4c0-.6.4-1 1-1h3.5c.6 0 1 .4 1 1 0 1.3.2 2.5.6 3.6.1.3 0 .7-.2 1z" fill="var(--white)"/></svg>
    </div>
    <div class="abs contact-label">CONTACT US AT</div>
    <div class="abs phone">514-362-0917</div>
  </section>

  <div class="side-label" style="top:614px">BACK</div>

  <section class="card card--back">
    <svg class="layer" viewBox="0 0 845 563" aria-hidden="true">
      <defs>
        <linearGradient id="headerBlue" x1="0" y1="0" x2="1" y2="0">
          <stop offset="0" stop-color="#2a64b2"/><stop offset=".5" stop-color="#5596dc"/><stop offset="1" stop-color="#2a64b2"/>
        </linearGradient>
      </defs>
      <path d="M0 0 H845 V115 C760 150 650 120 540 115 C430 110 330 145 220 135 C130 127 60 115 0 140 Z" fill="url(#headerBlue)"/>
      <path d="M0 168 C70 128 140 120 230 140 C330 160 440 118 540 122 C650 126 760 150 845 120 L845 138 C760 165 650 140 540 138 C440 136 330 175 230 156 C140 140 70 146 0 178 Z" fill="var(--green)"/>
      <path d="M0 180 C60 150 140 148 230 160 C330 175 440 140 540 142 C650 144 760 165 845 140 L845 563 L0 563 Z" fill="var(--white)"/>
      <path d="M120 200 C220 260 280 330 380 360 C470 390 560 470 700 500" stroke="var(--mist)" stroke-width="60" fill="none" stroke-linecap="round" opacity=".6"/>
    </svg>

    <div class="abs back-eyebrow">RESIDENTIAL · COMMERCIAL</div>
    <div class="abs back-title">Exterior Cleaning &amp; Maintenance</div>

    <div class="tile" style="left:28px;top:195px"><div class="tile__photo photo--siding-before" role="img" aria-label="House siding before washing"></div><span class="tile__tag">BEFORE</span></div>
    <div class="tile" style="left:225px;top:195px"><div class="tile__photo photo--siding-after" role="img" aria-label="House siding after washing"></div><span class="tile__tag">AFTER</span></div>
    <div class="tile" style="left:428px;top:195px"><div class="tile__photo photo--gutter-before" role="img" aria-label="Gutter full of leaves before cleaning"></div><span class="tile__tag">BEFORE</span></div>
    <div class="tile" style="left:624px;top:195px"><div class="tile__photo photo--gutter-after" role="img" aria-label="Clean gutter along shingle roof after cleaning"></div><span class="tile__tag">AFTER</span></div>
    <div class="tile" style="left:28px;top:342px"><div class="tile__photo photo--stone-before" role="img" aria-label="Stone steps before cleaning"></div><span class="tile__tag">BEFORE</span></div>
    <div class="tile" style="left:225px;top:342px"><div class="tile__photo photo--stone-after" role="img" aria-label="Stone steps after cleaning"></div><span class="tile__tag">AFTER</span></div>
    <div class="tile" style="left:428px;top:342px"><div class="tile__photo photo--deck-before" role="img" aria-label="Wooden porch deck before cleaning"></div><span class="tile__tag">BEFORE</span></div>
    <div class="tile" style="left:624px;top:342px"><div class="tile__photo photo--deck-after" role="img" aria-label="Wooden porch deck after cleaning"></div><span class="tile__tag">AFTER</span></div>

    <p class="abs intro">We are exterior cleaners that do everything from cleaning your homes to your business fronts.</p>
    <div class="abs mini-brand"><span class="brand__dot"></span><span>Summit</span></div>
  </section>
</div>
</body>
</html>
```